Weebly e-commerce website for 'brightmendwellhouse.com' small business.

We require an efficient and savvy website designer to help setup a Weebly e-commerce website. The domain name is 'brightmendwellhouse.com . As a small business with the latest international technology protocols in pain relief and function restoration, we wish to attract people with pain and health issues to our clinic and help provide information on good health. Products that promote this goal are to be sold in the online store. The logo for the business is being produced by a graphic designer and will be available 12th Sept. Colours are luminous green, azure blue and golden yellow. Fonts are to be striking and visible to the older generation, and the website is to be very user friendly and easy to navigate.

Pages for Site:

Home
About
Store/Shop
Links/Info

Target Market(s)

People with pain or health issues, or need function restoration, including elderly people.

Industry/Entity Type

E-Commerce

Number of Pages Required

5+ page

Font styles to use
Sans Serif

Colors
9bcb3b
fbed22
0492cd

Requirements
Must have
• Message able to be understood in 3 seconds

```html
<!DOCTYPE html>
<html lang="en">
<head>
<meta charset="utf-8">
<title>Brightmend Wellhouse – Store</title>
<link rel="stylesheet" href="https://fonts.googleapis.com/css2?family=Oswald:wght@300;400;500;700&family=Open+Sans:wght@400;600;700&display=swap">
<style>
:root{
  --green:#9bcb3b;
  --blue:#0492cd;
  --yellow:#fbed22;
  --dark:#1f240f;
  --page:#eef2ec;
  --white:#ffffff;
  --text:#555b55;
  --muted:#7a7f7a;
  --line:#dfe3de;
  --star:#1aa3e0;
}
*{margin:0;padding:0;box-sizing:border-box}
html,body{width:1080px;height:1200px;overflow:hidden}
body{background:var(--page);font-family:"Open Sans",sans-serif;color:var(--text);position:relative}
.abs{position:absolute}
.top-band{left:155px;top:0;width:768px;height:11px;background:var(--dark)}
.top-nav{right:163px;top:24px;display:flex;gap:17px;font-family:"Oswald",sans-serif;font-weight:300;font-size:12px;letter-spacing:.2px;color:#111}
.top-nav a{color:inherit;text-decoration:none}
.top-nav a.active{color:var(--green)}
.brand-name{left:164px;top:60px;font-family:"Oswald",sans-serif;font-weight:700;font-size:50px;color:var(--green);letter-spacing:-.5px}
.lock-btn{left:638px;top:124px;width:38px;height:36px;background:var(--dark);display:flex;align-items:center;justify-content:center}
.cart-bar{left:699px;top:123px;width:224px;height:38px;background:var(--green);display:flex;align-items:center;padding-left:9px;color:var(--white);font-family:"Oswald",sans-serif;font-weight:300}
.cart-bar .label{font-size:12px;margin-left:6px}
.cart-bar .count{font-size:10px;color:var(--dark);margin-left:17px;font-family:"Open Sans",sans-serif}
.cart-bar .caret{position:absolute;right:12px;top:16px}
.category-bar{left:155px;top:170px;width:768px;height:57px;background:var(--dark);display:flex}
.category-bar a{flex:1;display:flex;align-items:center;justify-content:center;color:var(--white);font-family:"Open Sans",sans-serif;font-size:10px;text-decoration:none;border-right:1px solid #3a3f2c}
.category-bar a:last-child{border-right:0}
.category-bar a.active{background:var(--green)}
.hero{left:155px;top:231px;width:768px;height:283px;background:var(--yellow)}
.hero-photo{position:absolute;left:0;top:0;width:540px;height:279px;background:linear-gradient(120deg,#d8b26a 0%,#6e9a3a 35%,#3e7a22 60%,#8c4a14 80%,#4e8a2a 100%)}
.hero-arrows{position:absolute;left:21px;top:236px;display:flex;gap:5px}
.hero-arrows span{width:25px;height:25px;background:var(--white);display:flex;align-items:center;justify-content:center}
.hero-promo{position:absolute;left:540px;top:0;width:228px;height:279px;background:var(--blue);text-align:center;color:var(--white)}
.hero-promo h2{font-family:"Oswald",sans-serif;font-weight:700;color:var(--yellow);font-size:40px;line-height:48px;margin-top:45px}
.hero-promo p{font-family:"Oswald",sans-serif;font-weight:300;font-size:13.5px;line-height:18px;margin-top:16px}
.shop-btn{display:inline-block;margin-top:32px;background:var(--white);color:#444;font-size:9px;padding:8px 13px}
.panel{background:var(--white);border:1px solid var(--line)}
.panel-head{height:32px;color:var(--white);font-weight:700;font-size:11.5px;display:flex;align-items:center;padding-left:19px;letter-spacing:.2px}
.panel-head.blue{background:var(--blue);border-bottom:2px solid #0580b4}
.panel-head.green{background:var(--green);padding-left:23px;border-bottom:2px solid #89b62f}
.brands{left:154px;top:550px;width:207px;height:144px}
.brands ul{list-style:none;padding:14px 0 0 20px;font-size:11.5px;color:var(--muted)}
.brands li{height:25.5px}
.offers{left:154px;top:723px;width:207px;height:411px}
.offer{position:absolute;left:14px;width:190px}
.offer .thumb{position:absolute;left:0;width:64px;height:60px;border-radius:3px}
.offer .info{position:absolute;left:86px;top:0;font-size:11.5px;color:var(--muted);line-height:14px}
.offer .price{margin-top:5px}
.offer .was{text-decoration:line-through;color:var(--muted)}
.offer .now{color:var(--blue);margin-left:5px}
.offer .stars{color:var(--star);font-size:14px;letter-spacing:-1px;line-height:16px}
.products{left:383px;top:550px;width:540px;height:584px}
.card{position:absolute;width:165px;height:244px;border:1px solid #eceeec;background:var(--white)}
.card .shot{position:absolute;left:50%;transform:translateX(-50%);top:12px;width:70px;height:128px;border-radius:10px}
.card h3{position:absolute;left:18px;top:152px;font-size:8.5px;font-weight:600;color:#5a5f5a}
.card p{position:absolute;left:18px;top:168px;width:140px;font-size:8.5px;line-height:11px;color:var(--muted)}
.card .price{position:absolute;left:13px;top:207px;font-family:"Oswald",sans-serif;font-weight:300;font-size:16px;color:var(--blue)}
.card .details{position:absolute;left:82px;top:207px;width:71px;height:21px;background:var(--green);display:flex;align-items:center;color:var(--white);font-family:"Oswald",sans-serif;font-size:8.5px;font-weight:500}
.card .details.dark{background:var(--dark)}
.card .details .ico{width:22px;height:21px;background:var(--blue);display:flex;align-items:center;justify-content:center;margin-right:6px}
.row2 h3{top:146px}.row2 p{top:162px}.row2 .price,.row2 .details{top:206px}
</style>
</head>
<body>
<div class="abs top-band"></div>
<nav class="abs top-nav"><a class="active" href="#">HOME</a><a href="#">ABOUT</a><a href="#">CONTACT</a></nav>
<div class="abs brand-name">Brightmend</div>
<div class="abs lock-btn"><svg width="14" height="16" viewBox="0 0 14 16"><path d="M3.5 7V5a3.5 3.5 0 0 1 7 0v2" fill="none" stroke="#fff" stroke-width="2"/><rect x="1" y="7" width="12" height="9" rx="1" fill="#fff"/></svg></div>
<div class="abs cart-bar">
  <svg width="26" height="24" viewBox="0 0 26 24"><path d="M1 2h4l3 13h13l3-9H7" fill="none" stroke="#fff" stroke-width="1.6"/><circle cx="10" cy="20" r="1.8" fill="#fff"/><circle cx="19" cy="20" r="1.8" fill="#fff"/></svg>
  <span class="label">Cart</span><span class="count">1 PRODUCT</span>
  <svg class="caret" width="8" height="5" viewBox="0 0 8 5"><path d="M0 0h8L4 5z" fill="#1f240f"/></svg>
</div>
<nav class="abs category-bar">
  <a href="#">CATEGORY</a><a class="active" href="#">CATEGORY</a><a href="#">CATEGORY</a><a href="#">CATEGORY</a><a href="#">CATEGORY</a><a href="#">CATEGORY</a><a href="#">CATEGORY</a>
</nav>
<section class="abs hero">
  <div class="hero-photo" role="img" aria-label="White pills spilling from an amber bottle onto a green leaf"></div>
  <div class="hero-arrows">
    <span><svg width="6" height="8" viewBox="0 0 6 8"><path d="M5 0L1 4l4 4" fill="none" stroke="#333" stroke-width="1.5"/></svg></span>
    <span><svg width="6" height="8" viewBox="0 0 6 8"><path d="M1 0l4 4-4 4" fill="none" stroke="#333" stroke-width="1.5"/></svg></span>
  </div>
  <div class="hero-promo">
    <h2>SALE UPTO<br>50%</h2>
    <p>Write Two or Three Lines About The<br>Special&nbsp; Promotion&nbsp; That You are Offering</p>
    <span class="shop-btn">SHOP NOW!</span>
  </div>
</section>
<aside class="abs panel brands">
  <div class="panel-head blue">BRANDS</div>
  <ul><li>Brand name one</li><li>Brand name two</li><li>Brand name three</li><li>Brand name four</li></ul>
</aside>
<aside class="abs panel offers">
  <div class="panel-head blue">SPECIAL OFFER</div>
  <div class="offer" style="top:40px">
    <div class="thumb" style="top:12px;background:linear-gradient(90deg,#2f7a3a,#e6e2c4)" role="img" aria-label="Natural deodorant box"></div>
    <div class="info">DETOX Natural<br>Medicine<div class="price"><span class="was">$20.00</span><span class="now">$15.00</span></div><div class="stars">★★★★</div></div>
  </div>
  <div class="offer" style="top:125px">
    <div class="thumb" style="top:8px;left:8px;width:46px;background:linear-gradient(90deg,#1c6fb5,#3aa04a)" role="img" aria-label="Fruit snack box"></div>
    <div class="info">DETOX Natural<br>Medicine<div class="price"><span class="was">$20.00</span><span class="now">$15.00</span></div><div class="stars">★★★</div></div>
  </div>
  <div class="offer" style="top:206px">
    <div class="thumb" style="top:10px;left:12px;width:38px;background:linear-gradient(90deg,#c8352a,#e9d9b4)" role="img" aria-label="Energy bar box"></div>
    <div class="info">DETOX Natural<br>Medicine<div class="price"><span class="was">$20.00</span><span class="now">$15.00</span></div><div class="stars">★★</div></div>
  </div>
  <div class="offer" style="top:298px">
    <div class="thumb" style="top:12px;left:8px;width:46px;background:linear-gradient(90deg,#1c6fb5,#3aa04a)" role="img" aria-label="Fruit snack box"></div>
    <div class="info">DETOX Natural<br>Medicine<div class="price"><span class="was">$20.00</span><span class="now">$15.00</span></div><div class="stars">★★★★</div></div>
  </div>
</aside>
<main class="abs panel products">
  <div class="panel-head green">NEW PRODUCTS</div>
  <div class="card" style="left:19px;top:48px">
    <div class="shot" style="background:linear-gradient(180deg,#f2f2f2,#fbe8a8 60%,#f4f4f4)" role="img" aria-label="White supplement bottle with floral label"></div>
    <h3>Detox Therapeutic Medicine</h3><p>It is very noble activity to protect health and help people to....</p>
    <span class="price">$15.65</span>
    <span class="details dark"><span class="ico"><svg width="13" height="11" viewBox="0 0 13 11"><path d="M0 1h2l2 6h7l1.5-4.5H3" fill="none" stroke="#fff" stroke-width="1.2"/><circle cx="5" cy="9.5" r="1" fill="#fff"/><circle cx="10" cy="9.5" r="1" fill="#fff"/></svg></span>DETAILS</span>
  </div>
  <div class="card" style="left:196px;top:48px">
    <div class="shot" style="width:54px;background:linear-gradient(180deg,#eee 0%,#1e1e1e 20%,#2e8a4a 65%,#1e1e1e 100%)" role="img" aria-label="Dark liquid medicine bottle with green label"></div>
    <h3>Fern Valley Medicine</h3><p>It is very noble activity to protect health and help people to....</p>
    <span class="price">$15.65</span>
    <span class="details"><span class="ico"><svg width="13" height="11" viewBox="0 0 13 11"><path d="M0 1h2l2 6h7l1.5-4.5H3" fill="none" stroke="#fff" stroke-width="1.2"/><circle cx="5" cy="9.5" r="1" fill="#fff"/><circle cx="10" cy="9.5" r="1" fill="#fff"/></svg></span>DETAILS</span>
  </div>
  <div class="card" style="left:374px;top:48px">
    <div class="shot" style="width:64px;background:linear-gradient(180deg,#f3f3f3 0%,#f3f3f3 35%,#d6e43a 40%,#c9d92c 85%,#f3f3f3 100%)" role="img" aria-label="Supplement bottle with yellow label"></div>
    <h3>Fern Valley Medicine</h3><p>It is very noble activity to protect health and help people to....</p>
    <span class="price">$15.65</span>
    <span class="details"><span class="ico"><svg width="13" height="11" viewBox="0 0 13 11"><path d="M0 1h2l2 6h7l1.5-4.5H3" fill="none" stroke="#fff" stroke-width="1.2"/><circle cx="5" cy="9.5" r="1" fill="#fff"/><circle cx="10" cy="9.5" r="1" fill="#fff"/></svg></span>DETAILS</span>
  </div>
  <div class="card row2" style="left:19px;top:308px">
    <div class="shot" style="background:linear-gradient(180deg,#eee,#e2ebd8 60%,#a8cc5a)" role="img" aria-label="White capsule bottle with green leaf label"></div>
    <h3>Fern Valley Medicine</h3><p>It is very noble activity to protect health and help people to....</p>
    <span class="price">$15.65</span>
    <span class="details"><span class="ico"><svg width="13" height="11" viewBox="0 0 13 11"><path d="M0 1h2l2 6h7l1.5-4.5H3" fill="none" stroke="#fff" stroke-width="1.2"/><circle cx="5" cy="9.5" r="1" fill="#fff"/><circle cx="10" cy="9.5" r="1" fill="#fff"/></svg></span>DETAILS</span>
  </div>
  <div class="card row2" style="left:197px;top:308px">
    <div class="shot" style="width:66px;background:linear-gradient(180deg,#1f6a44 0%,#1f6a44 18%,#f4f4f4 22%,#f4f4f4 100%)" role="img" aria-label="White mushroom supplement bottle with green cap"></div>
    <h3>Fern Valley Medicine</h3><p>It is very noble activity to protect health and help people to....</p>
    <span class="price">$15.65</span>
    <span class="details"><span class="ico"><svg width="13" height="11" viewBox="0 0 13 11"><path d="M0 1h2l2 6h7l1.5-4.5H3" fill="none" stroke="#fff" stroke-width="1.2"/><circle cx="5" cy="9.5" r="1" fill="#fff"/><circle cx="10" cy="9.5" r="1" fill="#fff"/></svg></span>DETAILS</span>
  </div>
  <div class="card row2" style="left:374px;top:308px">
    <div class="shot" style="width:124px;height:114px;background:linear-gradient(180deg,#1f6a44 0%,#1f6a44 18%,#f4f4f4 22%,#f4f4f4 100%)" role="img" aria-label="Two white mushroom supplement bottles with green caps"></div>
    <h3>Fern Valley Medicine</h3><p>It is very noble activity to protect health and help people to....</p>
    <span class="price">$15.65</span>
    <span class="details"><span class="ico"><svg width="13" height="11" viewBox="0 0 13 11"><path d="M0 1h2l2 6h7l1.5-4.5H3" fill="none" stroke="#fff" stroke-width="1.2"/><circle cx="5" cy="9.5" r="1" fill="#fff"/><circle cx="10" cy="9.5" r="1" fill="#fff"/></svg></span>DETAILS</span>
  </div>
</main>
</body>
</html>
```